Home brewer beer bottle label

I need a label for home-brew beer bottles. My sons and I all make our own beer. It should say Frask Ale in blackletter (because we are of German heritage) (EDIT: ACTUALLY WE ARE LIKING OTHER TYPEFACE NOW) and the designer will need to work in aspects of the Frask family (crest attached). Finally we will need two blank areas or lines for (1) what kind of beer (handwritten) and (2) who made it (the Hopwright!) I have attached a rough sketch, but feel free to ignore and be creative. No color requirements. (EDIT: ACTUALLY, MY WIFE LIKES THE LITTLE BIT OF PURPLE IN THE 4TH DESIGN) Would like the logotype portion of the label to be usable on its own as a family logo. (EDIT; THIS IS LESS IMPORTANT NOW). I have attached another file sketch, which shows using the parts of the family crest w/out trying to replicate it. Thanks, everyone, for the good work....
Updates

Project Deadline Extended
Reason: Extending because my wife is out of town until Wednesday and I need her input.

Target Market(s)

Mostly friends and family at the wedding.

Industry/Entity Type

Work

Font styles to use
Serif
Sans Serif

Requirements
Must have
• Tightly kerned lettering,
Nice to have
• Color, one Group of Elements in Indesign and the print file, "Beer" and "Hopwright" lines
Should not have
• Hard to see logo or logo type

```html
<!DOCTYPE html>
<html lang="en">
<head>
<meta charset="utf-8">
<title>Frask Ale – Bottle Labels</title>
<link rel="stylesheet" href="https://fonts.googleapis.com/css2?family=Ultra&family=Fira+Sans+Condensed:wght@600;700&display=swap">
<style>
  :root {
    --paper: #ffffff;
    --label-khaki: #cec680;
    --ink: #1c1a19;
    --band-blue: #2e47a6;
    --band-text: #d8cf7c;
    --crest-blue: #2f56a8;
    --crest-gold: #e0b93c;
  }
  * { margin: 0; padding: 0; box-sizing: border-box; }
  html, body {
    width: 1200px;
    height: 700px;
    overflow: hidden;
    background: var(--paper);
  }
  .canvas {
    position: relative;
    width: 1200px;
    height: 700px;
  }
  .label {
    position: absolute;
    top: 0;
    width: 578px;
    height: 700px;
    background: var(--label-khaki);
  }
  .label--square-shoulder { left: 0; }
  .label--round-shoulder { left: 622px; }
  .label__frame {
    position: absolute;
    inset: 0;
    width: 578px;
    height: 700px;
  }
  .label__frame path {
    fill: none;
    stroke: var(--ink);
    stroke-width: 9;
    stroke-linejoin: miter;
  }
  .label__crest {
    position: absolute;
    left: 152px;
    top: 66px;
    width: 280px;
    height: 280px;
    border-radius: 46% 46% 38% 38%;
    background: radial-gradient(ellipse at 50% 55%, var(--crest-blue) 0%, var(--crest-blue) 38%, var(--crest-gold) 70%, rgba(224,185,60,0) 100%);
  }
  .label__title {
    position: absolute;
    left: 30px;
    top: 352px;
    width: 518px;
    font-family: "Ultra", Georgia, serif;
    font-weight: 400;
    font-size: 96px;
    line-height: 100px;
    letter-spacing: -2px;
    color: var(--ink);
    text-align: center;
  }
  .label__band {
    position: absolute;
    left: 30px;
    top: 578px;
    width: 518px;
    height: 39px;
    background: var(--band-blue);
    color: var(--band-text);
    font-family: "Fira Sans Condensed", "Arial Narrow", sans-serif;
    font-weight: 700;
    font-size: 23px;
    line-height: 39px;
    text-align: center;
  }
  .label__field {
    position: absolute;
    top: 629px;
    font-family: "Fira Sans Condensed", "Arial Narrow", sans-serif;
    font-weight: 700;
    font-size: 22px;
    color: var(--ink);
  }
  .label__field--beer { left: 44px; }
  .label__field--maker { left: 306px; }
</style>
</head>
<body>
<main class="canvas">

  <section class="label label--square-shoulder">
    <svg class="label__frame" viewBox="0 0 578 700" aria-hidden="true">
      <path d="M30,667 V145 H92 A197,123 0 0 1 486,145 H548 V667 Z"/>
    </svg>
    <div class="label__crest" role="img" aria-label="Area reserved for the family crest artwork"></div>
    <h1 class="label__title">Frask<br>Ale</h1>
    <p class="label__band">Home-Brewed by the Frask Family</p>
    <p class="label__field label__field--beer">Beer</p>
    <p class="label__field label__field--maker">Hopwright</p>
  </section>

  <section class="label label--round-shoulder">
    <svg class="label__frame" viewBox="0 0 578 700" aria-hidden="true">
      <path d="M30,667 V272 Q30,250 52,250 H84 Q92,250 92,236 A197,214 0 0 1 486,236 Q486,250 494,250 H526 Q546,250 546,272 V667 Z"/>
    </svg>
    <div class="label__crest" role="img" aria-label="Area reserved for the family crest artwork"></div>
    <h2 class="label__title">Frask<br>Ale</h2>
    <p class="label__band">Home-Brewed by the Frask Family</p>
    <p class="label__field label__field--beer">Beer</p>
    <p class="label__field label__field--maker">Hopwright</p>
  </section>

</main>
</body>
</html>
```